Harwick Legal

To update and modernize current business card appearance. Marta's business is based in Melbourne with 4 other lawyers in the firm. Marta travels to the Pilbara in Western Australia approximately 1 week a month as part of the firms legal work. She consults with clients in Newman, Tom Price and Port Hedland. The lawyers work mostly from a home office, apart from court appearances. They have a virtual office in Melbourne city, and use facilities in 3 or 4 other locations around Melbourne. It is important the client's think this is a conventional law firm with a permanent office. Our business structure is a difficult concept for them to grasp. The business has been operational for 3 years, growing from 1 lawyer to 4 lawyers during that time. Our website is www.Harwicklegal.example.au and is currently being upgraded as we are not happy with its content. The logo is currently orange and dark grey but the orange is a difficult colour to reproduce and often turns out "poo" brown when documents are printed. We need clients to know we are user friendly and caring - and not head up our rears ends as some lawyers appear to be.
Updates

Thank you for the feedback so far. 1. Some of the designs have too much black (We prefer darker grey & not too much.) 2. Happy for designers to play around with different colours & logo design. What we're after is a modern look and business card that people say "wow" when they pick it up.

Industry/Entity Type

Business

```html
<!DOCTYPE html>
<html lang="en">
<head>
<meta charset="utf-8">
<title>Harwick Legal — Business Card</title>
<link rel="stylesheet" href="https://fonts.googleapis.com/css2?family=Arimo:ital,wght@0,400;0,700;1,400;1,700&display=swap">
<style>
  :root {
    --bg: #e9e7e4;
    --card: #ffffff;
    --ink: #1d1d1d;
    --band: #2e2f31;
    --orange: #e8834f;
    --rule: #2e2f31;
    --shadow: rgba(0, 0, 0, 0.18);
  }
  * { box-sizing: border-box; margin: 0; padding: 0; }
  html, body {
    width: 1200px;
    height: 900px;
    overflow: hidden;
    background: var(--bg);
    font-family: "Arimo", Arial, sans-serif;
    color: var(--ink);
  }
  .canvas { position: relative; width: 1200px; height: 900px; }

  .card {
    position: absolute;
    width: 560px;
    height: 320px;
    background: var(--card);
    border-radius: 26px;
    box-shadow: 0 14px 30px var(--shadow);
    overflow: hidden;
  }
  .card--back { left: 90px; top: 110px; }
  .card--front { left: 550px; top: 470px; }

  /* Wordmark */
  .wordmark {
    position: absolute;
    display: flex;
    align-items: center;
    gap: 14px;
  }
  .wordmark__dot {
    width: 54px;
    height: 54px;
    border-radius: 50%;
    background: var(--orange);
    flex: none;
  }
  .wordmark__name {
    font-weight: 700;
    font-size: 34px;
    letter-spacing: 1px;
    color: var(--ink);
    white-space: nowrap;
    padding-bottom: 6px;
    border-bottom: 1.5px solid var(--rule);
  }
  .card--back .wordmark { left: 92px; top: 128px; }
  .card--front .wordmark { left: 176px; top: 34px; }
  .card--front .wordmark__dot { width: 46px; height: 46px; }
  .card--front .wordmark__name { font-size: 30px; }

  /* Side band */
  .band { position: absolute; left: 0; top: 0; width: 170px; height: 320px; }

  /* Person */
  .person { position: absolute; left: 196px; top: 118px; }
  .person__name { font-weight: 700; font-size: 25px; }
  .person__role { font-style: italic; font-size: 19px; margin-top: 4px; }

  /* Contacts */
  .contacts {
    position: absolute;
    left: 176px;
    top: 208px;
    list-style: none;
    font-style: italic;
    font-size: 17px;
  }
  .contacts__item {
    display: flex;
    align-items: center;
    gap: 9px;
    height: 24px;
    white-space: nowrap;
  }
  .contacts__icon { width: 15px; height: 15px; flex: none; }
  .contacts__icon svg { width: 15px; height: 15px; display: block; }
</style>
</head>
<body>
<main class="canvas">

  <section class="card card--back" aria-label="Card back">
    <div class="wordmark">
      <span class="wordmark__dot"></span>
      <span class="wordmark__name">Harwick Legal</span>
    </div>
  </section>

  <section class="card card--front" aria-label="Card front">
    <svg class="band" viewBox="0 0 170 320" aria-hidden="true">
      <path d="M0 0 H118 C96 60 92 120 110 190 C122 240 118 285 108 320 H0 Z" fill="var(--band)"/>
      <path d="M118 0 H150 C126 60 120 120 138 190 C150 240 146 285 138 320 H108 C118 285 122 240 110 190 C92 120 96 60 118 0 Z" fill="var(--orange)"/>
    </svg>

    <div class="wordmark">
      <span class="wordmark__dot"></span>
      <span class="wordmark__name">Harwick Legal</span>
    </div>

    <div class="person">
      <p class="person__name">Daniel Reeve</p>
      <p class="person__role">Founder</p>
    </div>

    <ul class="contacts">
      <li class="contacts__item">
        <span class="contacts__icon"><svg viewBox="0 0 16 16"><rect x="4" y="1" width="8" height="14" rx="1.5" fill="none" stroke="var(--ink)" stroke-width="1.6"/><circle cx="8" cy="12.5" r="0.9" fill="var(--ink)"/></svg></span>
        03 9555 0142
      </li>
      <li class="contacts__item">
        <span class="contacts__icon"><svg viewBox="0 0 16 16"><rect x="1" y="3.5" width="14" height="9" fill="var(--ink)"/><path d="M1.5 4 L8 9 L14.5 4" fill="none" stroke="#fff" stroke-width="1.2"/></svg></span>
        daniel@harwicklegal.example.au
      </li>
      <li class="contacts__item">
        <span class="contacts__icon"><svg viewBox="0 0 16 16" fill="none" stroke="var(--ink)" stroke-width="1.3"><circle cx="8" cy="8" r="6.5"/><ellipse cx="8" cy="8" rx="3" ry="6.5"/><path d="M1.5 8 H14.5 M2.5 4.8 H13.5 M2.5 11.2 H13.5"/></svg></span>
        www.Harwicklegal.example.au
      </li>
      <li class="contacts__item">
        <span class="contacts__icon"><svg viewBox="0 0 16 16"><circle cx="8" cy="8" r="6.5" fill="var(--ink)"/></svg></span>
        @harwicklegal
      </li>
    </ul>
  </section>

</main>
</body>
</html>
```